Design some Business Cards for Heartland Trusted Business Power

I need a business card for Heartland Trusted Business Power. Attached is a flyer for The company. On the front of the card I would like:

1. The Heartland Trusted logo (found on the flyer)
2. My picture (attached )
3. Name: Desmond R. Falkner
4. Phone number: 914-382-6051
6. Address: 4087 Wexford Street, 2nd Floor
Bronx, New York 10562

On the back, at the top I would like, "Please Allow Me to Bid for Your Energy Contract"

Underneath that, use the bullet points found in the flyer under "What we can do for your business'

at the bottom add "No Switching fees, No interruption of Service, Just lower costs!"

```html
<!DOCTYPE html>
<html lang="en">
<head>
<meta charset="utf-8">
<title>Heartland Trusted Business Power – Business Card</title>
<link rel="stylesheet" href="https://fonts.googleapis.com/css2?family=Questrial&display=swap">
<style>
  :root {
    --navy: #1d3573;
    --navy-light: #2e53a3;
    --navy-deep: #152859;
    --red: #d8242b;
    --ink: #2a2a33;
    --white: #ffffff;
    --paper: #eceef2;
    --photo-light: #dbe6f3;
    --photo-mid: #9fb8d8;
  }
  * { box-sizing: border-box; margin: 0; padding: 0; }
  html, body {
    width: 1200px; height: 912px; overflow: hidden;
    background: var(--paper);
    font-family: "Questrial", "Century Gothic", sans-serif;
    color: var(--ink);
  }
  .card {
    position: absolute;
    left: 240px;
    width: 720px; height: 412px;
    background: var(--white);
    overflow: hidden;
    box-shadow: 0 6px 18px rgba(20, 30, 60, 0.18);
  }
  .card--front { top: 32px; }
  .card--back { top: 468px; }
  .card__shapes { position: absolute; inset: 0; }

  /* front */
  .brand {
    position: absolute; left: 26px; top: 48px;
    display: flex; align-items: center; gap: 10px;
  }
  .brand__square { width: 20px; height: 20px; background: var(--red); flex: none; }
  .brand__name {
    color: var(--navy); font-size: 18px; line-height: 1.2;
    letter-spacing: 0.5px; text-transform: uppercase;
  }
  .portrait {
    position: absolute; left: 392px; top: 28px;
    width: 290px; height: 172px; border-radius: 22px;
    border: 5px solid var(--white);
    background: linear-gradient(160deg, var(--photo-light), var(--photo-mid));
  }
  .person {
    position: absolute; left: 392px; top: 214px; width: 290px;
    text-align: right; color: var(--white);
  }
  .person__name { font-size: 27px; }
  .person__title { font-size: 16px; margin-top: 4px; }
  .contact {
    position: absolute; left: 30px; top: 304px;
    list-style: none; color: var(--white); font-size: 13px;
  }
  .contact li { display: flex; align-items: flex-start; gap: 9px; margin-bottom: 5px; line-height: 1.25; }
  .contact svg { flex: none; margin-top: 1px; }

  /* back */
  .pitch {
    position: absolute; left: 34px; top: 24px;
    color: var(--red); font-size: 22px;
  }
  .services-band {
    position: absolute; left: 30px; right: 30px; top: 60px; height: 40px;
    background: var(--navy); color: var(--white);
    font-size: 24px; text-align: center; line-height: 40px;
  }
  .benefits {
    position: absolute; left: 40px; right: 34px; top: 118px;
    list-style: none; font-size: 16px; line-height: 1.35;
  }
  .benefits li { display: flex; gap: 12px; margin-bottom: 14px; }
  .benefits svg { flex: none; margin-top: 3px; }
  .promise-band {
    position: absolute; left: 0; right: 0; bottom: 0; height: 58px;
    background: linear-gradient(90deg, var(--navy-deep), var(--navy-light));
    color: var(--white); font-size: 20px; text-align: center; line-height: 58px;
  }
</style>
</head>
<body>

<section class="card card--front">
  <svg class="card__shapes" width="720" height="412" viewBox="0 0 720 412">
    <defs>
      <linearGradient id="frontBlue" x1="0" y1="0" x2="1" y2="1">
        <stop offset="0" stop-color="#2e53a3"/>
        <stop offset="1" stop-color="#152859"/>
      </linearGradient>
    </defs>
    <path d="M340,0 H720 V412 H0 V282 C150,292 250,240 262,160 C274,80 290,20 340,0 Z" fill="url(#frontBlue)"/>
    <path d="M362,0 C314,22 300,80 288,160 C272,252 170,304 0,300" fill="none" stroke="#5c7fc4" stroke-width="3" opacity="0.6"/>
  </svg>

  <div class="brand">
    <span class="brand__square"></span>
    <span class="brand__name">Heartland<br>Trusted<br>Energy Services</span>
  </div>

  <div class="portrait" role="img" aria-label="Portrait photo of Desmond R. Falkner"></div>

  <div class="person">
    <p class="person__name">Desmond R. Falkner</p>
    <p class="person__title">Independent Consultant</p>
  </div>

  <ul class="contact">
    <li>
      <svg width="14" height="14" viewBox="0 0 14 14"><path d="M7 1 L13 6 H11 V13 H8 V9 H6 V13 H3 V6 H1 Z" fill="#fff"/></svg>
      <span>4087 Wexford Street, 2nd Floor<br>Bronx, New York 10562</span>
    </li>
    <li>
      <svg width="14" height="14" viewBox="0 0 14 14"><circle cx="7" cy="7" r="7" fill="#fff"/><path d="M4.5 3.5 L6 3.5 L6.6 5.5 L5.7 6.2 C6.2 7.3 6.8 7.9 7.8 8.4 L8.5 7.5 L10.5 8.1 L10.5 9.6 C7 9.8 4.3 7 4.5 3.5 Z" fill="#1d3573"/></svg>
      <span>914-382-6051</span>
    </li>
    <li>
      <svg width="14" height="14" viewBox="0 0 14 14"><circle cx="7" cy="7" r="7" fill="#fff"/><rect x="3.5" y="4.5" width="7" height="5" fill="none" stroke="#1d3573" stroke-width="1"/><path d="M3.5 4.5 L7 7.5 L10.5 4.5" fill="none" stroke="#1d3573" stroke-width="1"/></svg>
      <span>desmond@HeartlandTrustedPower.com</span>
    </li>
    <li>
      <svg width="14" height="14" viewBox="0 0 14 14"><circle cx="7" cy="7" r="7" fill="#fff"/><circle cx="7" cy="7" r="3.8" fill="none" stroke="#1d3573" stroke-width="1"/><path d="M3.2 7 H10.8 M7 3.2 V10.8" stroke="#1d3573" stroke-width="1"/></svg>
      <span>www.HeartlandTrustedPower.com</span>
    </li>
  </ul>
</section>

<section class="card card--back">
  <p class="pitch">Please Allow Me to Bid for Your Energy Contract</p>
  <div class="services-band">What We can Do for Your Business</div>

  <ul class="benefits">
    <li>
      <svg width="14" height="14" viewBox="0 0 14 14"><path d="M1 7.5 L5 11.5 L13 2.5" fill="none" stroke="#d8242b" stroke-width="3"/></svg>
      <span>We typically save our clients 10% to 30% off of current annual rates</span>
    </li>
    <li>
      <svg width="14" height="14" viewBox="0 0 14 14"><path d="M1 7.5 L5 11.5 L13 2.5" fill="none" stroke="#d8242b" stroke-width="3"/></svg>
      <span>At no cost to you, we analyze your bills to secure the best possible rate</span>
    </li>
    <li>
      <svg width="14" height="14" viewBox="0 0 14 14"><path d="M1 7.5 L5 11.5 L13 2.5" fill="none" stroke="#d8242b" stroke-width="3"/></svg>
      <span>we have pre-screened the premier suppliers in your market to protect you from costly mistakes</span>
    </li>
    <li>
      <svg width="14" height="14" viewBox="0 0 14 14"><path d="M1 7.5 L5 11.5 L13 2.5" fill="none" stroke="#d8242b" stroke-width="3"/></svg>
      <span>We offer price protection and budget certain!</span>
    </li>
  </ul>

  <div class="promise-band">No Switching fees, No interruptionsof Service, Just lower costs!</div>
</section>

</body>
</html>
```